Life Coaching and Career Coaching company needs new website with bold, modern, videos

We need a whole new website that is heavy on video. We are a small company who sells personal wellbeing services like career coaching, life coaching, and group coaching programs. The programs all help people design a better life.
FULL BRIEF ATTACHED and STYLE GUIDE
Also, look at https://www.brightfennel.com/coaching and galdrove.com and https://www.marnwick.life/ for a small amount of inspiration.

Industry/Entity Type

personal well-being/life coaching/career coaching

Number of Pages Required

3 page

Other font styles liked:
• fonts are in the brief

Requirements
Must have
• read the brief please - it's all in there. (things like the look, feel, how it will have lots of video, etc,)
Nice to have
• something really different looking and breakthrough. visually stunning. very trustworthy. Please read the brief, its all in there.
Should not have
• should not look like other life coaching websites. must have video!

```html
<!DOCTYPE html>
<html lang="en">
<head>
<meta charset="utf-8">
<title>Northway Living — Life &amp; Career Coaching</title>
<link href="https://fonts.googleapis.com/css2?family=Fredoka:wght@500;600&family=Poppins:wght@300;400;500&display=swap" rel="stylesheet">
<style>
:root{
  --coral:#f06562;
  --coral-soft:#f7a09e;
  --ink:#1d1d1f;
  --grey:#6b6b6b;
  --light:#9a9a9a;
  --white:#ffffff;
  --footer:#050505;
  --display:"Fredoka",sans-serif;
  --body:"Poppins",sans-serif;
}
*{box-sizing:border-box;margin:0;padding:0}
html,body{width:1200px;height:3699px;overflow:hidden;background:var(--white);font-family:var(--body);color:var(--ink)}
.page{position:relative;width:1200px;height:3699px;overflow:hidden}
.abs{position:absolute}

/* header */
.nav{position:absolute;top:0;left:0;width:1200px;height:107px;background:var(--white);z-index:3}
.brand{position:absolute;left:173px;top:22px;display:flex;align-items:center;gap:8px;font-family:var(--body);font-weight:400;font-size:24px;letter-spacing:1px;color:#6e6e6e}
.brand-mark{width:12px;height:12px;background:var(--coral)}
.menu{position:absolute;left:0;top:33px;width:820px;height:20px;font-size:12px;color:#555;white-space:nowrap}
.menu span{position:absolute;top:0}
.menu .active{color:var(--coral);font-weight:500}
.menu .active::before{content:"";position:absolute;left:50%;top:-10px;width:6px;height:6px;border-left:2px solid var(--coral);border-top:2px solid var(--coral);transform:translateX(-50%) rotate(45deg)}
.cta-top{position:absolute;left:825px;top:17px;width:202px;height:44px;border-radius:4px;background:var(--coral);color:var(--white);font-family:var(--display);font-weight:500;font-size:13px;display:flex;align-items:center;padding-left:58px;white-space:nowrap}
.cta-top svg{position:absolute;left:16px;top:10px}

/* hero */
.hero{position:absolute;top:75px;left:0;width:1200px;height:690px;border-radius:0 0 50% 50%/0 0 76px 76px;overflow:hidden;background:linear-gradient(100deg,#9a9a8c 0%,#c9c2b5 35%,#d9cfc3 55%,#b98a7a 75%,#8f7a6c 100%)}
.hero-shade{position:absolute;inset:0;background:linear-gradient(90deg,rgba(0,0,0,.28),rgba(0,0,0,.05) 70%)}
.follow{position:absolute;left:44px;top:245px;color:var(--white);font-size:11px;writing-mode:vertical-rl}
.follow-line{position:absolute;left:51px;top:315px;width:1px;height:52px;background:var(--white)}
.follow-dot{position:absolute;left:45px;width:12px;height:12px;border-radius:50%;background:var(--white)}
.hero-kicker{position:absolute;left:174px;top:239px;color:var(--white);font-family:var(--display);font-size:13px;font-weight:500}
.hero-title{position:absolute;left:172px;top:265px;width:720px;color:var(--white);font-family:var(--display);font-weight:600;font-size:38px;line-height:52px}
.hero-btn{position:absolute;left:174px;top:389px;width:238px;height:48px;border-radius:24px;background:var(--coral);color:var(--white);font-family:var(--display);font-weight:500;font-size:14px;display:flex;align-items:center;padding-left:26px;white-space:nowrap}
.hero-btn svg{position:absolute;right:22px;top:17px}
.hero-play{position:absolute;left:920px;top:255px;width:100px;height:100px;border-radius:50%;background:rgba(240,101,98,.35)}
.hero-play span{position:absolute;left:15px;top:15px;width:70px;height:70px;border-radius:50%;background:var(--coral)}
.hero-play svg{position:absolute;left:40px;top:38px}
.scroll-down{position:absolute;left:575px;top:740px;width:50px;height:50px;border-radius:50%;background:var(--coral);z-index:2}
.scroll-down svg{position:absolute;left:17px;top:19px}

/* section heads */
.kicker{position:absolute;left:0;width:1200px;text-align:center;font-size:12px;color:var(--grey)}
.title{position:absolute;left:0;width:1200px;text-align:center;font-family:var(--display);font-weight:600;font-size:27px;color:var(--ink)}

/* program tiles */
.tile{position:absolute;border-radius:4px;overflow:hidden}
.tile .label{position:absolute;left:25px;bottom:22px;color:var(--white);font-family:var(--display);font-weight:600;font-size:19px;white-space:nowrap}
.tile .shade{position:absolute;inset:0;background:linear-gradient(180deg,rgba(0,0,0,0) 55%,rgba(0,0,0,.45))}
.play{position:absolute;width:44px;height:44px;border-radius:50%;background:var(--white)}
.play svg{position:absolute;left:17px;top:15px}
.other-title{position:absolute;left:174px;top:1625px;font-family:var(--display);font-weight:600;font-size:27px;line-height:38px}
.mini{position:absolute;top:1603px;width:199px;height:167px;border-radius:4px;overflow:hidden;color:var(--white);font-family:var(--display);font-weight:600;font-size:17px;line-height:30px;text-align:center}
.mini .veil{position:absolute;inset:0;background:rgba(0,0,0,.35)}
.mini p{position:absolute;left:0;width:100%;top:50px}

/* process */
.process{position:absolute;left:0;top:1813px;width:1200px;height:422px;background:var(--coral)}
.process .kicker{color:var(--white)}
.process .title{color:var(--white)}
.step{position:absolute;top:146px;width:198px;height:193px;background:var(--white);border-radius:3px;text-align:center;overflow:hidden}
.step svg{position:absolute;left:75px;top:26px}
.step h3{position:absolute;top:94px;left:0;width:100%;font-family:var(--display);font-weight:600;font-size:13px}
.step p{position:absolute;top:124px;left:18px;width:162px;font-size:10px;line-height:17px;color:#444}
.step .num{position:absolute;left:0;width:100%;top:160px;font-family:var(--display);font-weight:600;font-size:32px;color:#fbd5d4}

/* story */
.story-photo{position:absolute;left:172px;top:2310px;width:388px;height:430px;background:linear-gradient(135deg,#e6e2dc,#d6cdbf 50%,#3f5b52 80%,#2a2f35)}
.story-frame{position:absolute;left:560px;top:2343px;width:22px;height:397px;border:1px solid #e3e3e3;border-left:none}
.chevrons{position:absolute;left:602px;top:2648px}
.story-kicker{position:absolute;left:652px;top:2362px;font-size:12px;color:var(--grey)}
.story-title{position:absolute;left:652px;top:2389px;font-family:var(--display);font-weight:600;font-size:27px}
.story-text{position:absolute;left:652px;top:2440px;width:376px;font-size:11.5px;line-height:22.5px;color:#666;font-weight:300}
.story-btn{position:absolute;left:653px;top:2638px;width:236px;height:43px;border-radius:22px;background:var(--coral);color:var(--white);font-family:var(--display);font-weight:500;font-size:15px;display:flex;align-items:center;padding-left:23px;white-space:nowrap}
.story-btn svg{position:absolute;right:22px;top:15px}

/* testimonials */
.client{position:absolute;top:2920px;width:270px;height:327px;overflow:hidden}
.client .who{position:absolute;left:0;bottom:0;width:150px;height:51px;background:var(--white);padding:10px 0 0 4px}
.client .who b{display:block;font-family:var(--display);font-weight:500;font-size:13px;white-space:nowrap}
.client .who small{font-size:10px;color:#555}
.client .play{left:131px;top:137px}
.dots{position:absolute;top:3284px;left:572px;display:flex;gap:13px}
.dots i{width:10px;height:10px;border-radius:50%;border:1px solid #999;display:block}
.dots i.on{background:var(--coral);border-color:var(--coral)}

/* footer */
.footer{position:absolute;left:-100px;top:3337px;width:1400px;height:420px;background:var(--footer);border-radius:50% 50% 0 0/80px 80px 0 0}
.f-brand{position:absolute;left:176px;top:3450px;display:flex;align-items:center;gap:8px;font-size:24px;letter-spacing:1px;color:#cfcfcf}
.f-col{position:absolute;top:3456px;font-size:11.5px;color:#8a8a8a;line-height:26.5px;white-space:nowrap}
.f-col h4{font-family:var(--body);font-weight:400;font-size:14px;color:#bdbdbd;margin-bottom:10px}
.f-contact{display:flex;align-items:center;gap:18px}
.copy{position:absolute;left:176px;top:3655px;font-size:10.5px;color:#3e3e3e}
.f-follow{position:absolute;left:884px;top:3652px;display:flex;align-items:center;gap:8px;font-size:10.5px;color:#3e3e3e}
.f-follow i{width:19px;height:19px;border-radius:50%;background:#6a6a6a;display:block}
</style>
</head>
<body>
<div class="page">

  <section class="hero">
    <div role="img" aria-label="Photo of two women talking over coffee in a bright living room" class="abs" style="inset:0"></div>
    <div class="hero-shade"></div>
    <div class="follow">Follow us</div>
    <div class="follow-line"></div>
    <span class="follow-dot" style="top:380px"></span>
    <span class="follow-dot" style="top:400px"></span>
    <span class="follow-dot" style="top:420px"></span>
    <div class="hero-kicker">watch a first coaching session &nbsp;›</div>
    <h1 class="hero-title">Only Northway Living offers both life and career coaching programs</h1>
    <a class="hero-btn">Explore Our Programs
      <svg width="10" height="14" viewBox="0 0 10 14"><path d="M2 1l6 6-6 6" fill="none" stroke="#fff" stroke-width="2.2"/></svg></a>
    <div class="hero-play"><span></span>
      <svg width="20" height="24" viewBox="0 0 20 24"><path d="M2 2l16 10-16 10z" fill="#fff"/></svg></div>
  </section>

  <header class="nav">
    <div class="brand"><span class="brand-mark"></span>NORTHWAY</div>
    <nav class="menu">
      <span class="active" style="left:397px">Home</span>
      <span style="left:459px">About us</span>
      <span style="left:540px">Our Programs</span>
      <span style="left:646px">Our Team</span>
      <span style="left:727px">Contact Us</span>
    </nav>
    <a class="cta-top">
      <svg width="26" height="24" viewBox="0 0 26 24"><path d="M3 3h14a2 2 0 012 2v8a2 2 0 01-2 2H9l-5 4v-4H3a2 2 0 01-2-2V5a2 2 0 012-2z" fill="#fff"/><path d="M21 8h2a2 2 0 012 2v6a2 2 0 01-2 2h-1v3l-4-3h-5" fill="none" stroke="#fff" stroke-width="1.5"/></svg>
      Make An Appointment</a>
  </header>

  <div class="scroll-down"><svg width="16" height="12" viewBox="0 0 16 12"><path d="M2 2l6 6 6-6" fill="none" stroke="#fff" stroke-width="2.5"/></svg></div>

  <p class="kicker" style="top:817px">What We do</p>
  <h2 class="title" style="top:842px">Our Special Programs</h2>

  <div class="tile" style="left:174px;top:909px;width:344px;height:315px;background:linear-gradient(135deg,#b9b1a6,#8b98a8 60%,#55667d)" role="img" aria-label="Photo of a coach talking with a smiling client">
    <div class="shade"></div><div class="play" style="left:150px;top:131px"><svg width="12" height="14" viewBox="0 0 12 14"><path d="M1 1l10 6-10 6z" fill="#f06562"/></svg></div><span class="label">Life Coaching</span></div>
  <div class="tile" style="left:538px;top:909px;width:490px;height:315px;background:linear-gradient(135deg,#d9d3ca,#c8bfb2 50%,#8a7f78)" role="img" aria-label="Photo of a career coaching session in an office">
    <div class="shade"></div><div class="play" style="left:222px;top:131px"><svg width="12" height="14" viewBox="0 0 12 14"><path d="M1 1l10 6-10 6z" fill="#f06562"/></svg></div><span class="label">Career Coaching</span></div>
  <div class="tile" style="left:171px;top:1244px;width:491px;height:316px;background:linear-gradient(135deg,#ecebe8,#d8d6d2 60%,#9a9690)" role="img" aria-label="Photo of a group coaching circle in a studio">
    <div class="shade"></div><div class="play" style="left:222px;top:132px"><svg width="12" height="14" viewBox="0 0 12 14"><path d="M1 1l10 6-10 6z" fill="#f06562"/></svg></div><span class="label">Group Coaching</span></div>
  <div class="tile" style="left:683px;top:1244px;width:345px;height:316px;background:linear-gradient(135deg,#c9d2d6,#8c7a6e 50%,#3d4f67)" role="img" aria-label="Photo of a couple in a relationship coaching session">
    <div class="shade"></div><div class="play" style="left:150px;top:132px"><svg width="12" height="14" viewBox="0 0 12 14"><path d="M1 1l10 6-10 6z" fill="#f06562"/></svg></div><span class="label">Relationship Coaching</span></div>

  <h3 class="other-title">Other<br>Coaching<br>Programs</h3>
  <div class="mini" style="left:393px;background:linear-gradient(135deg,#7c7f86,#4a4e55)" role="img" aria-label="Photo of a group workshop"><div class="veil"></div><p>4 Weeks<br>Program</p></div>
  <div class="mini" style="left:611px;background:linear-gradient(135deg,#c7c9cc,#7d8288)" role="img" aria-label="Photo of a one to one session"><div class="veil"></div><p>7 Weeks<br>Program</p></div>
  <div class="mini" style="left:830px;background:linear-gradient(135deg,#2e3a4a,#9a6a45 60%,#1f2630)" role="img" aria-label="Photo of hikers helping each other at sunset"><div class="veil"></div><p>12 Weeks<br>Program</p></div>

  <section class="process">
    <p class="kicker" style="top:50px">Our Process</p>
    <h2 class="title" style="top:77px">How it Works</h2>
    <div class="step" style="left:172px">
      <svg width="48" height="48" viewBox="0 0 48 48" fill="none" stroke="#f06562" stroke-width="1.6"><rect x="4" y="3" width="28" height="40" rx="2"/><path d="M10 11h6v5h-6zM10 21h6v5h-6zM10 31h6v5h-6zM20 13h8M20 23h8M20 33h6"/><path d="M34 30l9 4v9l-9 4-9-4v-9z"/></svg>
      <h3>Choose a service</h3><p>Lorem ipsum dolor sit amet, consectetur adipiscing elit ft,</p><span class="num">01</span></div>
    <div class="step" style="left:392px">
      <svg width="48" height="48" viewBox="0 0 48 48" fill="none" stroke="#f06562" stroke-width="1.6"><circle cx="24" cy="12" r="7"/><circle cx="10" cy="20" r="5"/><circle cx="38" cy="20" r="5"/><path d="M12 44V30a12 12 0 0124 0v14M2 44V34a8 8 0 018-8M46 44V34a8 8 0 00-8-8M2 44h44"/></svg>
      <h3>Book a career coach</h3><p>Lorem ipsum dolor sit amet, consectetur adipiscing elit ft,</p><span class="num">02</span></div>
    <div class="step" style="left:609px">
      <svg width="50" height="50" viewBox="0 0 50 50" fill="none" stroke="#f06562" stroke-width="1.6"><rect x="3" y="7" width="38" height="32" rx="2"/><path d="M3 15h38M12 3v8M32 3v8M9 21h5v4H9zM18 21h5v4h-5zM27 21h5v4h-5zM9 29h5v4H9z"/><circle cx="38" cy="38" r="9"/><path d="M34 38l3 3 5-6"/></svg>
      <h3>Decide on a time</h3><p>Lorem ipsum dolor sit amet, consectetur adipiscing elit ft,</p><span class="num">03</span></div>
    <div class="step" style="left:828px">
      <svg width="50" height="50" viewBox="0 0 50 50" fill="none" stroke="#f06562" stroke-width="1.6"><path d="M46 4c-12 0-22 6-28 18l10 10c12-6 18-16 18-28z"/><circle cx="34" cy="16" r="4"/><path d="M18 22l-8 1-6 7 10 1M28 32l-1 8-7 6-1-10M14 36l-8 8M10 30l-6 6M20 40l-6 6"/></svg>
      <h3>Get started!</h3><p>Lorem ipsum dolor sit amet, consectetur adipiscing elit ft,</p><span class="num">04</span></div>
  </section>

  <div class="story-photo" role="img" aria-label="Photo of two women laughing together on a sofa with a dog"></div>
  <div class="story-frame"></div>
  <svg class="chevrons" width="16" height="92" viewBox="0 0 16 92" fill="none" stroke="#f7a09e" stroke-width="2"><path d="M2 10l6-6 6 6M2 24l6-6 6 6M2 38l6-6 6 6M2 52l6-6 6 6M2 66l6-6 6 6M2 80l6-6 6 6"/></svg>
  <p class="story-kicker">Our Story</p>
  <h2 class="story-title">Who We Are</h2>
  <p class="story-text">Lorem ipsum dolor sit amet, consectetur adipiscing elit, sed do eiusmod tempor incididunt ut labore et dolore magna aliqua. Ut enim ad minim veniam, quis nostrud exercitation ullamco laboris nisi ut aliquip ex ea commodo consequat. Duis aute irure dolor in reprehenderit in voluptate velit esse cillum dolore eu fugiat nulla pariatur. Excepteur sint occaecat cupidatat non proident, sunt in culpa qui officia deserunt mollit anim id est laborum.</p>
  <a class="story-btn">Make An Appointment
    <svg width="10" height="14" viewBox="0 0 10 14"><path d="M2 1l6 6-6 6" fill="none" stroke="#fff" stroke-width="2.2"/></svg></a>

  <p class="kicker" style="top:2828px">Our Success stories</p>
  <h2 class="title" style="top:2850px">Client Testimonials</h2>

  <div class="client" style="left:174px;background:linear-gradient(160deg,#4b5a52,#a8b4c2 60%,#3a3f46)" role="img" aria-label="Portrait of a smiling woman in a denim jacket">
    <div class="play"><svg width="12" height="14" viewBox="0 0 12 14"><path d="M1 1l10 6-10 6z" fill="#f06562"/></svg></div>
    <div class="who"><b>Lena Hartley</b><small>Managing Director</small></div></div>
  <div class="client" style="left:465px;background:linear-gradient(160deg,#9c9c9a,#5d6a78 60%,#2b3440)" role="img" aria-label="Portrait of a smiling man with curly hair">
    <div class="play"><svg width="12" height="14" viewBox="0 0 12 14"><path d="M1 1l10 6-10 6z" fill="#f06562"/></svg></div>
    <div class="who"><b>Tomas Verhoek</b><small>Managing Director</small></div></div>
  <div class="client" style="left:755px;background:linear-gradient(160deg,#c99a4a,#6b5c4a 55%,#1e1e24)" role="img" aria-label="Portrait of a woman in a dark blazer outdoors">
    <div class="play"><svg width="12" height="14" viewBox="0 0 12 14"><path d="M1 1l10 6-10 6z" fill="#f06562"/></svg></div>
    <div class="who"><b>Sofia Marchetti</b><small>Managing Director</small></div></div>

  <div class="dots"><i></i><i class="on"></i><i></i></div>

  <footer class="footer"></footer>
  <div class="f-brand"><span class="brand-mark"></span>NORTHWAY</div>
  <div class="f-col" style="left:419px"><h4>Office</h4>Germany —<br>212 Linden Row, Suite 9<br>Hamburg, De 20095</div>
  <div class="f-col" style="left:643px"><h4>Our Programs</h4>Life Coaching<br>Career Coaching<br>Relationship Coaching<br>Group Coaching</div>
  <div class="f-col" style="left:851px"><h4>Phone &amp; Email address</h4>
    <div class="f-contact"><svg width="13" height="10" viewBox="0 0 13 10"><rect width="13" height="10" rx="1" fill="#8a8a8a"/><path d="M1 1l5.5 4L12 1" fill="none" stroke="#050505"/></svg>hello@northwayliving.com</div>
    <div class="f-contact"><svg width="13" height="13" viewBox="0 0 13 13"><path d="M3 1l2 3-1.5 1.5a8 8 0 004 4L9 8l3 2-1 2.5C6 13 0 7 .5 2z" fill="#8a8a8a"/></svg>+1 555 014 27 38</div></div>
  <p class="copy">© 2024 Northwayliving.com. All Rights Reserved.</p>
  <div class="f-follow">Follow Us : <i></i><i></i><i></i></div>

</div>
</body>
</html>
```